BoltCrest Screw Box and Carton Design

We are BoltCrest, a new screw and nail supplier from Ireland. We need box designs branded for our new launch of screws and nails, Outer carton and inner individual boxes. We would like our branding to portray the image of a professional company. We have our logo attached which we would like to stand out so that people recognise the box if it were to be seen from a distance or in a shop.

Target Market(s)

Construction Industry

Industry/Entity Type

Construction

Contact Information for Business Card

Declan Murtagh
Owner
07482316907
declan@boltcrest.co.uk

Font styles to use
Sans Serif

Colors
3277b5

Requirements
Must have
• The Carton should be cost effective for the box maker. The carton will contain 10 boxes. If you could design them in such a way that they can be manipulated easily to cater for the various sizes. The internal boxes that hold the screws will have colour. I like the layout of the Korvik box where the lid folds out over the front of the box. Blue colour #009ee2 Grey colour #4a4a49
Nice to have
• I would like some upgraded design to the original BoltCrest box in the picture. I feel that this design does not cater well for labels or information to be placed on the box.

```html
<!DOCTYPE html>
<html lang="en">
<head>
<meta charset="utf-8">
<title>BoltCrest Screw Box Dieline</title>
<link rel="stylesheet" href="https://fonts.googleapis.com/css2?family=Lato:wght@700;900&display=swap">
<style>
  :root {
    --grey: #4a4a49;
    --blue: #009ee2;
    --white: #ffffff;
    --ink: #000000;
  }
  html, body {
    margin: 0;
    padding: 0;
    width: 1003px;
    height: 1200px;
    overflow: hidden;
    background: var(--white);
  }
  .dieline-sheet { display: block; width: 1003px; height: 1200px; }
  .bg-grey { fill: var(--grey); }
  .bg-blue { fill: var(--blue); }
  .cut-lines { fill: none; stroke-width: 2.2; stroke-linejoin: miter; }
  .cut-lines--light { stroke: var(--white); }
  .cut-lines--dark { stroke: var(--ink); }
  .brand-name {
    font-family: "Lato", sans-serif;
    font-weight: 900;
    fill: var(--white);
  }
  .brand-tagline {
    font-family: "Lato", sans-serif;
    font-weight: 700;
    fill: var(--white);
    font-size: 20px;
  }
  .address-block {
    font-family: "Lato", sans-serif;
    font-weight: 700;
    fill: var(--white);
    font-size: 15px;
  }
  .info-label {
    font-family: "Lato", sans-serif;
    font-weight: 700;
    fill: var(--ink);
    font-size: 15px;
  }
  .info-area { fill: var(--white); }
  .safety-badge { fill: var(--white); }
  .safety-glyph { fill: none; stroke: var(--grey); stroke-width: 4; stroke-linecap: round; }
</style>
</head>
<body>
<svg class="dieline-sheet" viewBox="0 0 1254 1500" xmlns="http://www.w3.org/2000/svg">
  <defs>
    <clipPath id="blue-zone"><polygon points="63,1300 1190,415 1190,1437 63,1437"/></clipPath>
    <clipPath id="grey-zone"><polygon points="63,63 1190,63 1190,415 63,1300"/></clipPath>
    <g id="dieline">
      <!-- top flaps -->
      <rect x="153" y="113" width="284" height="214"/>
      <path d="M437,327 L437,113 L447,102 L813,102 L825,114 L825,114 L813,114 L813,327 L827,342 L428,342 L437,327 Z"/>
      <rect x="813" y="114" width="287" height="213"/>
      <!-- upper body row -->
      <rect x="428" y="342" width="399" height="288"/>
      <rect x="153" y="447" width="275" height="188"/>
      <rect x="827" y="447" width="273" height="186"/>
      <rect x="251" y="612" width="84" height="23"/>
      <rect x="917" y="612" width="86" height="20"/>
      <!-- middle row -->
      <rect x="155" y="635" width="275" height="225"/>
      <rect x="430" y="630" width="392" height="243"/>
      <rect x="822" y="633" width="278" height="227"/>
      <!-- lower row -->
      <path d="M153,873 L430,873 L430,1095 L332,1095 L325,1101 L257,1101 L250,1095 L153,1095 Z"/>
      <rect x="430" y="873" width="395" height="287"/>
      <path d="M822,873 L1100,873 L1100,1093 L1003,1093 L995,1101 L927,1101 L919,1093 L822,1093 Z"/>
      <!-- bottom panel and rounded dust flaps -->
      <rect x="435" y="1160" width="383" height="237"/>
      <path d="M435,1163 L260,1163 C215,1170 200,1210 202,1240 C205,1330 290,1385 355,1392 L435,1392"/>
      <path d="M818,1163 L995,1163 C1040,1170 1057,1210 1055,1240 C1050,1330 970,1385 905,1392 L818,1392"/>
    </g>
  </defs>

  <rect class="bg-grey" x="63" y="63" width="1127" height="1374"/>
  <polygon class="bg-blue" points="63,1300 1190,415 1190,1437 63,1437"/>
  <polygon class="bg-grey" points="610,1160 818,1160 818,1397 795,1397"/>
  <path class="bg-grey" d="M818,1163 L995,1163 C1040,1170 1057,1210 1055,1240 C1050,1330 970,1385 905,1392 L818,1392 Z"/>

  <g class="cut-lines cut-lines--light" clip-path="url(#grey-zone)"><use href="#dieline"/></g>
  <g class="cut-lines cut-lines--dark" clip-path="url(#blue-zone)"><use href="#dieline"/></g>

  <!-- safety notices on lid -->
  <g class="safety-notices" aria-label="Wear eye and ear protection">
    <circle class="safety-badge" cx="490" cy="170" r="25"/>
    <rect class="safety-glyph" x="475" y="162" width="30" height="14" rx="6"/>
    <circle class="safety-badge" cx="554" cy="170" r="25"/>
    <path class="safety-glyph" d="M540,180 L540,168 A14,14 0 0 1 568,168 L568,180"/>
  </g>

  <!-- company address -->
  <text class="address-block" x="612" y="389">BOLTCREST</text>
  <text class="address-block" x="612" y="427">1234 Any Avenue</text>
  <text class="address-block" x="612" y="446">Any city, Any country</text>
  <text class="address-block" x="612" y="484">boltcrest.co.uk</text>

  <!-- large vertical brand name -->
  <text class="brand-name" transform="translate(548,1395) rotate(-90)" font-size="152" textLength="765" lengthAdjust="spacingAndGlyphs">BOLTCREST</text>

  <!-- inverted brand names on inner panels -->
  <text class="brand-name" transform="translate(290,795) rotate(180)" font-size="38" text-anchor="middle" textLength="182" lengthAdjust="spacingAndGlyphs">BOLTCREST</text>
  <text class="brand-name" transform="translate(692,795) rotate(180)" font-size="38" text-anchor="middle" textLength="182" lengthAdjust="spacingAndGlyphs">BOLTCREST</text>

  <!-- front brand name -->
  <text class="brand-name" x="692" y="939" font-size="38" text-anchor="middle" textLength="182" lengthAdjust="spacingAndGlyphs">BOLTCREST</text>

  <!-- lid front -->
  <text class="brand-name" x="692" y="1299" font-size="40" text-anchor="middle" textLength="188" lengthAdjust="spacingAndGlyphs">BOLTCREST</text>
  <text class="brand-tagline" x="697" y="1317" text-anchor="middle">SCREWS AND NAILS</text>

  <!-- information label area -->
  <rect class="info-area" x="846" y="679" width="226" height="156"/>
  <text class="info-label" transform="translate(958,786) rotate(180)" text-anchor="middle">AREA</text>
  <text class="info-label" transform="translate(958,803) rotate(180)" text-anchor="middle">INFORMATION</text>
</svg>
</body>
</html>
```